We need a business card design for our website qvwtrading.net. The Star Headline is qvwtrading.net, in large lettering.We sell fashion rings of titanium, mirror pollished stainless steel, and related jewelry. Basically quality products competing with the high expense of gold.We have to portray honesty and trust, because thats who I am. I know marketing, but I am weak on colors and layout. 3D Gold curved edge letters are ok. No green and yellow.Black,Red,Purple and White in small amounts.No fancy Lettering.
No Rainbows in printing.
Our goal is selling our products online globally

Kind Regards Maren Tulloch

Fashion

qvwtrading.net
known for our ideal fit rings
email.marentullochptyltd@corvexmail com

```html
<!DOCTYPE html>
<html lang="en">
<head>
<meta charset="utf-8">
<title>QVW Trading – Business Card</title>
<link rel="stylesheet" href="https://fonts.googleapis.com/css2?family=Michroma&display=swap">
<style>
  :root {
    --page-bg: #d9d9d9;
    --card-black: #141414;
    --card-grey: #2a2a2a;
    --gold: #c9a43e;
    --white: #f2f2f2;
  }
  html, body {
    margin: 0;
    width: 1200px;
    height: 900px;
    overflow: hidden;
    background: var(--page-bg);
  }
  .business-card {
    position: absolute;
    left: 180px;
    top: 210px;
    width: 840px;
    height: 480px;
    background:
      radial-gradient(ellipse at 30% 25%, var(--card-grey) 0%, transparent 55%),
      radial-gradient(ellipse at 75% 80%, #222 0%, transparent 50%),
      var(--card-black);
    box-shadow: 0 12px 30px rgba(0,0,0,0.35);
    font-family: "Michroma", sans-serif;
    color: var(--white);
    text-align: center;
  }
  .brand-name {
    position: absolute;
    top: 118px;
    left: 0;
    right: 0;
    margin: 0;
    font-size: 56px;
    font-weight: 400;
    letter-spacing: 1px;
    color: var(--gold);
  }
  .tagline {
    position: absolute;
    top: 200px;
    left: 0;
    right: 0;
    margin: 0;
    font-size: 15px;
    letter-spacing: 5px;
    text-transform: uppercase;
  }
  .contact {
    position: absolute;
    top: 320px;
    left: 0;
    right: 0;
    margin: 0;
    font-size: 15px;
    letter-spacing: 4px;
    line-height: 30px;
    text-transform: uppercase;
  }
</style>
</head>
<body>
  <section class="business-card">
    <h1 class="brand-name">QVWTRADING</h1>
    <p class="tagline">Known for our ideal fit rings</p>
    <p class="contact">
      <span class="contact-web">www.qvwtrading.net</span><br>
      <span class="contact-email">marentullochptyltd@corvexmail com</span>
    </p>
  </section>
</body>
</html>
```